Bright Meadow Dental - Stationary
Business Cards, Letterhead, & Envelope
Project: Bright Meadow Dental - Stationary
Bright Meadow Dental - Stationary - Health
Creative Brief
Professional
Leland Fisk, D.D.S.
3847 W Thornbury Ln, Suite 2 Fairhaven, KS 66215
BrightMeadowDental@mailbox-example.com
www.BrightMeadowDental-example.com
We're a fun office and want people to expect great cosmetic work and accommodations for families. We don't need a "blow your mind" presentation, just something classy.

```html
<!DOCTYPE html>
<html lang="en">
<head>
<meta charset="utf-8">
<title>Bright Meadow Dental – Stationery</title>
<link rel="stylesheet" href="https://fonts.googleapis.com/css2?family=Open+Sans:wght@400;600;700&display=swap">
<style>
  :root {
    --bg: #e9ebee;
    --paper: #ffffff;
    --brand-blue: #1b5fae;
    --brand-navy: #0c2a5a;
    --band-light: #3a86d4;
    --text-grey: #5a6270;
    --shadow: 0 2px 8px rgba(20, 30, 50, 0.18);
  }
  * { box-sizing: border-box; margin: 0; padding: 0; }
  html, body {
    width: 1200px; height: 876px; overflow: hidden;
    background: var(--bg);
    font-family: "Open Sans", Arial, sans-serif;
    color: var(--text-grey);
  }
  .canvas { position: relative; width: 1200px; height: 876px; }
  .piece { position: absolute; background: var(--paper); box-shadow: var(--shadow); overflow: hidden; }

  .wordmark { color: var(--brand-blue); font-weight: 700; letter-spacing: 0.02em; line-height: 1.1; white-space: nowrap; }
  .wordmark .dot { display: inline-block; width: 0.55em; height: 0.55em; border-radius: 50%; background: var(--brand-blue); margin-right: 0.35em; vertical-align: 0.05em; }
  .tagline { color: var(--brand-navy); font-weight: 600; white-space: nowrap; }

  /* business card front */
  .card-front { left: 40px; top: 40px; width: 260px; height: 152px; border-radius: 10px; }
  .card-front .wordmark { position: absolute; left: 16px; top: 14px; font-size: 14px; }
  .card-front .tagline { position: absolute; left: 28px; top: 34px; font-size: 7px; }
  .name-band {
    position: absolute; left: 0; top: 56px; width: 100%; height: 34px;
    background: linear-gradient(180deg, var(--band-light), var(--brand-blue) 55%, var(--brand-navy));
    color: #fff; font-size: 12px; font-weight: 700; padding: 9px 0 0 58px; white-space: nowrap;
  }
  .name-band .credential { font-weight: 400; }
  .card-front .address { position: absolute; left: 12px; top: 100px; font-size: 5.5px; line-height: 1.6; white-space: nowrap; }
  .card-front .contacts { position: absolute; left: 116px; top: 100px; font-size: 5.5px; line-height: 1.6; white-space: nowrap; }

  /* business card back */
  .card-back {
    left: 316px; top: 40px; width: 260px; height: 152px; border-radius: 10px;
    background: radial-gradient(circle at 60% 40%, var(--band-light), var(--brand-blue) 45%, var(--brand-navy));
  }
  .card-back .wordmark { position: absolute; left: 50%; transform: translateX(-50%); top: 64px; font-size: 15px; color: #fff; }
  .card-back .wordmark .dot { background: #fff; }

  /* #10 envelope */
  .envelope { left: 40px; top: 218px; width: 536px; height: 232px; }
  .envelope .wordmark { position: absolute; left: 26px; top: 24px; font-size: 17px; }
  .envelope .tagline { position: absolute; left: 26px; top: 48px; font-size: 8px; }
  .envelope .address { position: absolute; left: 26px; top: 68px; font-size: 8px; line-height: 1.45; white-space: nowrap; }

  /* small envelope */
  .note { left: 40px; top: 476px; width: 536px; height: 360px; }
  .note .wordmark { position: absolute; left: 26px; top: 28px; font-size: 20px; }
  .note .tagline { position: absolute; left: 26px; top: 56px; font-size: 9px; }
  .note .address { position: absolute; left: 26px; bottom: 34px; font-size: 8px; white-space: nowrap; }
  .footer-bar { position: absolute; left: 0; bottom: 0; width: 100%; height: 8px; background: var(--brand-blue); border-top: 3px solid var(--brand-navy); }

  /* letterhead */
  .letterhead { left: 606px; top: 40px; width: 554px; height: 796px; }
  .letterhead .wordmark { position: absolute; left: 50%; transform: translateX(-50%); top: 42px; font-size: 20px; }
  .letterhead .tagline { position: absolute; width: 100%; text-align: center; top: 70px; font-size: 9px; }
  .letterhead .footer-line {
    position: absolute; left: 0; bottom: 20px; width: 100%; text-align: center;
    font-size: 6.5px; white-space: nowrap;
  }
  .letterhead .footer-line span { margin: 0 4px; }
</style>
</head>
<body>
<main class="canvas">

  <section class="piece card-front" aria-label="Business card front">
    <div class="wordmark"><span class="dot"></span>Bright Meadow Dental</div>
    <div class="tagline">Gentle Care for Every Smile</div>
    <div class="name-band">Leland Fisk <span class="credential">| D.D.S.</span></div>
    <div class="address">3847 W Thornbury Ln, Suite 2<br>Fairhaven, KS 66215</div>
    <div class="contacts">
      P: 555-014-2290<br>
      F: 555-014-2291<br>
      BrightMeadowDental@mailbox-example.com<br>
      www.BrightMeadowDental-example.com
    </div>
  </section>

  <section class="piece card-back" aria-label="Business card back">
    <div class="wordmark"><span class="dot"></span>Bright Meadow Dental</div>
  </section>

  <section class="piece envelope" aria-label="Envelope">
    <div class="wordmark"><span class="dot"></span>Bright Meadow Dental</div>
    <div class="tagline">Gentle Care for Every Smile</div>
    <div class="address">3847 W Thornbury Ln, Suite 2<br>Fairhaven, KS 66215</div>
  </section>

  <section class="piece note" aria-label="Small envelope">
    <div class="wordmark"><span class="dot"></span>Bright Meadow Dental</div>
    <div class="tagline">Gentle Care for Every Smile</div>
    <div class="address">3847 W Thornbury Ln, Suite 2 Fairhaven, KS 66215</div>
    <div class="footer-bar"></div>
  </section>

  <section class="piece letterhead" aria-label="Letterhead">
    <div class="wordmark"><span class="dot"></span>Bright Meadow Dental</div>
    <div class="tagline">Gentle Care for Every Smile</div>
    <div class="footer-line">
      <span>3847 W Thornbury Ln, Suite 2 Fairhaven, KS 66215</span>
      <span>P: 555-014-2290</span>
      <span>BrightMeadowDental@mailbox-example.com</span>
      <span>www.BrightMeadowDental-example.com</span>
    </div>
    <div class="footer-bar"></div>
  </section>

</main>
</body>
</html>
```